Corvanto Card

The logo is the Spanish flag colors I want a vibrant eye catching design with the yellow / red colors over either Navy or white background or black even ,
Would like a 2D feel to the logo with another lighter color logo under it look ,

Contact Information for Business Card

Corvanto Flooring
Tobias Renwick
Main Number
Cell Number
Fax Number

Website on the side of the card somewhere

Font styles to use
Sans Serif

Colors
ec1f27
ffc214

Requirements
Must have
• 2 logos feel one is bolder and the other one underneath very light

```html
<!DOCTYPE html>
<html lang="en">
<head>
<meta charset="utf-8">
<title>Corvanto Flooring – Business Card</title>
<link href="https://fonts.googleapis.com/css2?family=Saira:wght@400;500;700&display=swap" rel="stylesheet">
<style>
  :root{
    --page:#e9e6e1;
    --card-dark:#1c1c1c;
    --card-dark-glow:#3a3a3a;
    --card-light:#ddd4c9;
    --card-light-2:#eae3d9;
    --accent-red:#92201f;
    --accent-gold:#d6a12c;
    --icon-orange:#d98a1c;
    --ink:#1f1a17;
  }
  html,body{margin:0;padding:0;}
  body{
    width:1200px;height:969px;overflow:hidden;
    background:var(--page);
    font-family:"Saira",Arial,sans-serif;
    position:relative;
  }
  .card{
    position:absolute;left:100px;top:199px;
    width:1000px;height:571px;
    background:linear-gradient(135deg,var(--card-light-2),var(--card-light));
    box-shadow:0 14px 40px rgba(0,0,0,.25);
    overflow:hidden;
  }
  .card-shapes{position:absolute;inset:0;}
  .brand{
    position:absolute;left:0;top:326px;width:500px;
    text-align:center;margin:0;
    color:var(--accent-gold);
    font-weight:500;font-size:34px;letter-spacing:6px;
    text-transform:uppercase;
  }
  .brand-echo{
    position:absolute;right:18px;bottom:34px;margin:0;
    color:var(--accent-red);opacity:.16;
    font-weight:700;font-size:88px;line-height:1;letter-spacing:2px;
    text-transform:uppercase;
  }
  .contact{position:absolute;left:606px;top:154px;}
  .contact-name{
    margin:0;color:var(--accent-red);
    font-weight:700;font-size:33px;line-height:1;letter-spacing:-.3px;
  }
  .contact-role{
    margin:6px 0 0;color:var(--accent-gold);
    font-weight:400;font-size:21px;line-height:1;
  }
  .contact-list{list-style:none;margin:36px 0 0;padding:0;}
  .contact-list li{
    display:flex;align-items:center;gap:12px;
    height:28.5px;font-size:23px;color:var(--ink);
  }
  .contact-list svg{width:20px;height:20px;flex:none;fill:var(--icon-orange);}
</style>
</head>
<body>
  <section class="card">
    <svg class="card-shapes" viewBox="0 0 1000 571" width="1000" height="571" aria-hidden="true">
      <defs>
        <radialGradient id="darkGlow" cx="0.5" cy="0.3" r="0.8">
          <stop offset="0" stop-color="var(--card-dark-glow)"/>
          <stop offset="1" stop-color="var(--card-dark)"/>
        </radialGradient>
      </defs>
      <rect class="panel-dark" x="0" y="0" width="500" height="571" fill="url(#darkGlow)"/>
      <polygon class="divider-notch" points="500,139 556,187 500,235" fill="#0e0e0e"/>
      <polygon class="divider-band" fill="var(--accent-red)"
        points="500,0 516,0 516,135 574,187 516,239 516,571 500,571 500,235 556,187 500,139"/>
      <polygon class="divider-arrow" points="518,170 536,187 518,204" fill="var(--icon-orange)"/>
    </svg>

    <p class="brand">Corvanto Flooring</p>
    <p class="brand-echo" aria-hidden="true">Corvanto</p>

    <div class="contact">
      <h1 class="contact-name">TOBIAS RENWICK</h1>
      <p class="contact-role">President</p>
      <ul class="contact-list">
        <li><svg viewBox="0 0 24 24"><path d="M6.6 10.8a15 15 0 0 0 6.6 6.6l2.2-2.2a1 1 0 0 1 1-.25 11.4 11.4 0 0 0 3.6.57 1 1 0 0 1 1 1V20a1 1 0 0 1-1 1A17 17 0 0 1 3 4a1 1 0 0 1 1-1h3.5a1 1 0 0 1 1 1c0 1.25.2 2.45.57 3.57a1 1 0 0 1-.25 1z"/></svg>555-214-7730</li>
        <li><svg viewBox="0 0 24 24"><path d="M7 2h10a2 2 0 0 1 2 2v16a2 2 0 0 1-2 2H7a2 2 0 0 1-2-2V4a2 2 0 0 1 2-2zm0 3v12h10V5zm5 13.5a1 1 0 1 0 0 2 1 1 0 0 0 0-2z"/></svg>555-318-4062</li>
        <li><svg viewBox="0 0 24 24"><path d="M7 3h10v5H7zM4 9h16a2 2 0 0 1 2 2v7h-3v3H5v-3H2v-7a2 2 0 0 1 2-2zm3 7v3h10v-3z"/></svg>555-406-9125</li>
        <li><svg viewBox="0 0 24 24"><path d="M3 5h18v14H3zm2 2v.5l7 5 7-5V7zm0 3v7h14v-7l-7 5z"/></svg>info@corvanto.com</li>
        <li><svg viewBox="0 0 24 24"><circle cx="12" cy="12" r="9"/></svg>www.corvanto.com</li>
      </ul>
    </div>
  </section>
</body>
</html>
```